IT Company need facebook graphics

We need a facebook logo and cover that matches more our website and other marketing materials which is quite uniform in colours.
We are a small company, we do not advertise much mainly word of mouth, but we want to try out some Facebook advertising and need our page to look amazing.
Something playful yet professional, something that will stand out in peoples mind.
Target Market(s)
Home users and small business
Industry/Entity Type
Computer Repair
Requirements
Must have
- A colour scheme to match existing website, but be playful and fun. Website is www.mzpalisade.com.au
Nice to have
- No input for nice to have, I trust the awesome talent out there to come up with something.
Should not have
- Again, no input for should not haves.

```html
<!DOCTYPE html>
<html lang="en">
<head>
<meta charset="utf-8">
<title>MZ Palisade – Facebook Graphics</title>
<link href="https://fonts.googleapis.com/css2?family=Oswald:wght@400;500;600&family=Open+Sans:wght@400;600;700;800&display=swap" rel="stylesheet">
<style>
:root{
  --brand-red:#e8202a;
  --stage-dark:#151515;
  --stage-mid:#222;
  --white:#fff;
  --fb-grey:#e9ebee;
  --fb-line:#dddfe2;
  --fb-text:#1d2129;
  --fb-muted:#90949c;
  --fb-blue:#4267b2;
  --fb-green:#42b72a;
  --photo-warm:#c9a98a;
  --photo-cool:#3d4f73;
}
*{box-sizing:border-box;margin:0;padding:0}
html,body{width:1200px;height:1000px;overflow:hidden}
body{
  position:relative;
  background:radial-gradient(ellipse at 50% 40%,var(--stage-mid),var(--stage-dark) 75%);
  font-family:"Open Sans",Arial,sans-serif;
}
.piece{position:absolute}
.caption{position:absolute;color:var(--white);font-size:19px;font-weight:600;text-align:center;width:240px}
.wordmark{font-family:"Oswald",sans-serif;font-weight:600;letter-spacing:.5px;line-height:1}

/* display pictures */
.avatar{width:168px;height:168px;display:flex;align-items:center;justify-content:center}
.avatar::after{content:"";position:absolute;inset:6px;border:1px solid currentColor;pointer-events:none}
.avatar--light{background:linear-gradient(135deg,#fff,#ececec);color:var(--brand-red);left:122px;top:111px}
.avatar--red{background:var(--brand-red);color:var(--white);left:122px;top:357px;width:170px;height:170px;border:2px solid #c5141d}
.avatar .wordmark{font-size:26px}

/* page preview */
.page{left:343px;top:111px;width:735px;height:416px;background:var(--fb-grey);overflow:hidden}
.page-side{position:absolute;left:0;top:0;width:141px;height:100%}
.page-avatar{position:absolute;left:11px;top:8px;width:121px;height:121px;background:var(--brand-red);border:3px solid var(--white);display:flex;align-items:center;justify-content:center;color:var(--white)}
.page-avatar .wordmark{font-size:18px}
.page-name{position:absolute;left:11px;top:137px;font-size:16px;color:var(--fb-text)}
.page-handle{position:absolute;left:11px;top:157px;font-size:10px;color:var(--fb-muted)}
.page-nav{position:absolute;left:10px;top:184px;width:123px;list-style:none}
.page-nav li{font-size:10px;color:#4b4f56;height:22.8px;line-height:22.8px;padding-left:8px}
.page-nav li.is-active{background:#dcdee3;border-left:2px solid var(--fb-blue);font-weight:700;color:var(--fb-text)}
.page-create{position:absolute;left:16px;top:354px;background:var(--fb-green);color:#fff;font-size:9px;font-weight:700;padding:3px 6px;border-radius:2px}
.page-cover{position:absolute;left:141px;top:0;width:594px;height:222px}
.action-bar{position:absolute;left:141px;top:222px;width:594px;height:41px;background:#fff;border-bottom:1px solid var(--fb-line)}
.action-bar .btn{position:absolute;top:8px;height:20px;border:1px solid #ccd0d5;background:#f6f7f9;font-size:9px;font-weight:700;color:#4b4f56;line-height:18px;text-align:center}
.action-bar .btn--call{left:376px;width:204px;background:var(--fb-blue);border-color:var(--fb-blue);color:#fff}
.card{position:absolute;background:#fff;border:1px solid var(--fb-line)}
.composer{left:141px;top:268px;width:357px;height:78px}
.composer .tabs{height:22px;border-bottom:1px solid var(--fb-line);background:#f6f7f9;font-size:9px;font-weight:700;color:#4b4f56;padding:5px 10px}
.composer .tabs span{margin-right:14px}
.composer .tabs .link{color:var(--fb-blue)}
.composer .avatar-dot{position:absolute;left:8px;top:32px;width:28px;height:28px;background:#b7a08a}
.composer .prompt{position:absolute;left:45px;top:41px;font-size:10px;color:var(--fb-muted)}
.post{left:141px;top:354px;width:357px;height:70px}
.post .mini{position:absolute;left:8px;top:8px;width:28px;height:28px;border:1px solid var(--fb-line);color:var(--brand-red);display:flex;align-items:center;justify-content:center}
.post .mini .wordmark{font-size:6px}
.post .head{position:absolute;left:42px;top:9px;font-size:9.5px;color:var(--fb-muted)}
.post .head b{color:#365899}
.post .time{position:absolute;left:42px;top:24px;font-size:8px;color:var(--fb-muted)}
.post .body{position:absolute;left:8px;top:45px;font-size:9.5px;color:var(--fb-text)}
.side-info{left:506px;top:268px;width:224px;height:61px;padding:8px 8px;font-size:9.5px;color:var(--fb-text)}
.side-info .rating{color:var(--fb-blue);font-size:11px;margin-top:4px}
.side-search{left:506px;top:340px;width:224px;height:25px;font-size:9.5px;color:var(--fb-muted);padding:5px 22px}
.side-reply{left:506px;top:375px;width:224px;height:45px;font-size:8.5px;color:var(--fb-green);padding:8px 40px}

/* cover */
.cover{left:186px;top:614px;width:828px;height:315px}
</style>
</head>
<body>

<svg width="0" height="0" style="position:absolute" aria-hidden="true">
  <defs>
    <linearGradient id="photoTone" x1="0" y1="0" x2="1" y2="1">
      <stop offset="0" stop-color="#8f7b69"/>
      <stop offset=".45" stop-color="#c9a98a"/>
      <stop offset="1" stop-color="#3d4f73"/>
    </linearGradient>
    <linearGradient id="panelTone" x1="0" y1="0" x2="0" y2="1">
      <stop offset="0" stop-color="#fff"/>
      <stop offset="1" stop-color="#e9e9e9"/>
    </linearGradient>
    <symbol id="coverArt" viewBox="0 0 828 315">
      <g font-family="'Open Sans', Arial, sans-serif">
        <rect width="828" height="315" fill="url(#panelTone)"/>
        <polygon points="0,0 356,0 278,315 0,315" fill="url(#photoTone)" role="img" aria-label="Photo of a smiling family using a laptop together at home"/>
        <polygon points="356,0 370,0 292,315 278,315" fill="#e8202a"/>
        <text x="41" y="300" fill="#fff" font-family="Oswald, sans-serif" font-weight="500" font-size="30" textLength="188" lengthAdjust="spacingAndGlyphs">CALL : 1300 555 019</text>
        <text x="538" y="55" text-anchor="middle" fill="#e8202a" font-size="21">MZ Palisade</text>
        <polygon points="344,66 622,66 610,119 332,119" fill="#e8202a"/>
        <text x="361" y="110" fill="#fff" font-size="44" font-weight="800" textLength="242" lengthAdjust="spacingAndGlyphs">EXPERTISE</text>
        <text x="754" y="56" text-anchor="middle" fill="#e8202a" font-size="20" font-weight="600" font-family="Oswald, sans-serif">MZ PALISADE</text>
        <g fill="none" stroke="#666" stroke-width="2">
          <g transform="translate(395,185)">
            <polygon points="-22,-4 0,-26 22,-4" fill="#888"/>
            <rect x="-16" y="-4" width="32" height="26" fill="#e2e2e2"/>
            <rect x="-5" y="8" width="10" height="14" fill="#e8202a" stroke="none"/>
            <path d="M18,16 q16,6 4,14"/>
          </g>
          <g transform="translate(521,182)">
            <path d="M-16,-16 a10,10 0 0 1 10,-14 a13,13 0 0 1 22,4 a8,8 0 0 1 0,10 z" fill="#d8ecfa" stroke="#3a8fd0"/>
            <path d="M0,-16 v12 M-22,-4 h44 M-22,-4 v6 M22,-4 v6" stroke="#3a8fd0"/>
            <rect x="-34" y="2" width="24" height="16" fill="#3a8fd0" stroke="none"/>
            <rect x="10" y="2" width="24" height="16" fill="#3a8fd0" stroke="none"/>
          </g>
          <g transform="translate(654,184)">
            <polygon points="-36,-2 -12,-26 12,-2" fill="#888"/>
            <rect x="-30" y="-2" width="36" height="24" fill="#e2e2e2"/>
            <rect x="-4" y="-4" width="36" height="22" fill="#2f6fb5" stroke="#555"/>
            <path d="M-10,22 h48" stroke="#555" stroke-width="3"/>
          </g>
          <g transform="translate(765,184)">
            <polygon points="-10,-6 10,-26 30,-6" fill="#888"/>
            <rect x="-4" y="-6" width="28" height="26" fill="#e2e2e2"/>
            <circle cx="-6" cy="0" r="16" fill="#2f6fb5" stroke="#1d4c85"/>
            <path d="M-22,0 h32 M-6,-16 v32" stroke="#8fbdea" stroke-width="1.5"/>
          </g>
        </g>
        <g fill="#e8202a" font-size="12.5">
          <text x="335" y="233" textLength="120" lengthAdjust="spacingAndGlyphs">Residential computer /</text>
          <text x="356" y="250" textLength="78" lengthAdjust="spacingAndGlyphs">network issues</text>
          <text x="466" y="233" textLength="108" lengthAdjust="spacingAndGlyphs">Business computer /</text>
          <text x="482" y="250" textLength="78" lengthAdjust="spacingAndGlyphs">network issues</text>
          <text x="604" y="233" textLength="99" lengthAdjust="spacingAndGlyphs">Home Networking</text>
          <text x="735" y="233" textLength="61" lengthAdjust="spacingAndGlyphs">New Home</text>
          <text x="735" y="250" textLength="64" lengthAdjust="spacingAndGlyphs">Networking</text>
        </g>
        <text x="370" y="297" fill="#e8202a" font-size="13.5" textLength="404" lengthAdjust="spacingAndGlyphs">www.mzpalisade.com.au  | support@mzpalisade.com.au</text>
      </g>
    </symbol>
  </defs>
</svg>

<div class="piece avatar avatar--light"><span class="wordmark">MZ PALISADE</span></div>
<p class="caption" style="left:86px;top:294px">Display Picture 1</p>
<div class="piece avatar avatar--red"><span class="wordmark">MZ PALISADE</span></div>
<p class="caption" style="left:86px;top:534px">Display Picture 1</p>

<div class="piece page">
  <div class="page-side">
    <div class="page-avatar"><span class="wordmark">MZ PALISADE</span></div>
    <p class="page-name">MZ Palisade</p>
    <p class="page-handle">@mzpalisadetas</p>
    <ul class="page-nav">
      <li class="is-active">Home</li><li>About</li><li>Photos</li><li>Reviews</li><li>Likes</li><li>Videos</li><li>Posts</li>
    </ul>
    <span class="page-create">Create a Page</span>
  </div>
  <svg class="page-cover" viewBox="0 0 828 315" preserveAspectRatio="none"><use href="#coverArt"/></svg>
  <div class="action-bar">
    <span class="btn" style="left:10px;width:46px">Like</span>
    <span class="btn" style="left:56px;width:66px">Message</span>
    <span class="btn" style="left:122px;width:50px">Save</span>
    <span class="btn" style="left:172px;width:56px">··· More ▾</span>
    <span class="btn btn--call">Call Now</span>
  </div>
  <div class="card composer">
    <div class="tabs"><span>Status</span><span class="link">Photo / Video</span></div>
    <div class="avatar-dot"></div>
    <p class="prompt">Write something on this Page...</p>
  </div>
  <div class="card post">
    <div class="mini"><span class="wordmark">MZ PALISADE</span></div>
    <p class="head"><b>MZ Palisade</b> shared <b>Brightline Studio</b>'s video.</p>
    <p class="time">August 27 at 10:39am · ◦</p>
    <p class="body">A great look at how new tech can help kids learn at home</p>
  </div>
  <div class="card side-info">
    <p>Computer Service · Rosemount Bay, Tasmania, Australia</p>
    <p class="rating">5.0 ★★★★★</p>
  </div>
  <div class="card side-search">Search for posts on this Page</div>
  <div class="card side-reply">Very responsive to messages</div>
</div>

<svg class="piece cover" viewBox="0 0 828 315"><use href="#coverArt"/></svg>
<p class="caption" style="left:480px;top:926px;font-weight:400">Cover Photo</p>

</body>
</html>
```